Business Card Design - BVN (company name)

Over 20 years of progressive technology design, migration and management experience that drives business objectives and streamlines operations. Continuously challenge conventions to meet and exceed business security, availability and functionality requirements. Maintain exceptional vendor relationships to ensure ongoing knowledge of emerging products and to secure preferred service agreements. Recruit and utilize top talent and foster a collegial environment that advances innovation and performance excellence. design logo using 3 arrows of different colors green, gold, blue

Industry/Entity Type

Progressive

Contact Information for Business Card

Martin K. Osei
IT Strategist / Consultant

555.302.8846 MOsei@bvnorel.example 3817 Wrenfield Court Pasadena, CA 91877

Colors
0255a3
f37122
fece3e

Requirements
Must have
• Note NEW EMAIL ADDRESS
• MOsei@bvnorel.example
• NOTE NEW ORDER of the work I do.
• Infrastructure – Systems – Cybersecurity
Nice to have
• main color should be orange

```html
<!DOCTYPE html>
<html lang="en">
<head>
<meta charset="UTF-8">
<title>Torvane Business Card</title>
<link rel="stylesheet" href="https://fonts.googleapis.com/css2?family=Source+Sans+3:wght@400;600&display=swap">
<style>
  :root {
    --backdrop: #2f2f2f;
    --card-white: #ffffff;
    --brand-orange: #ee7d2e;
    --accent-orange: #f37122;
    --text-grey: #8a8a8a;
    --peach: #f8cfae;
    --back-text: #ffffff;
  }
  html, body {
    margin: 0;
    padding: 0;
    width: 1200px;
    height: 900px;
    overflow: hidden;
    background: var(--backdrop);
    font-family: "Source Sans 3", "Myriad Pro", Arial, sans-serif;
  }
  .stage {
    position: relative;
    width: 1200px;
    height: 900px;
  }
  .card {
    position: absolute;
    border-radius: 18px;
  }
  .card-front {
    left: 330px;
    top: 121px;
    width: 551px;
    height: 320px;
    background: var(--card-white);
  }
  .card-back {
    left: 330px;
    top: 505px;
    width: 555px;
    height: 322px;
    background: var(--brand-orange);
  }
  .brand-mark {
    position: absolute;
    left: 33px;
    top: 60px;
    display: flex;
    align-items: center;
    gap: 10px;
  }
  .brand-dot {
    width: 16px;
    height: 16px;
    border-radius: 50%;
    background: var(--accent-orange);
  }
  .brand-name {
    font-size: 40px;
    font-weight: 600;
    color: var(--accent-orange);
    line-height: 1;
  }
  .address {
    position: absolute;
    left: 24px;
    top: 155px;
    font-size: 17px;
    line-height: 18px;
    color: var(--text-grey);
  }
  .contact-list {
    position: absolute;
    left: 22px;
    top: 232px;
    margin: 0;
    padding: 0;
    list-style: none;
    font-size: 17px;
    color: var(--text-grey);
  }
  .contact-list li {
    display: flex;
    align-items: center;
    gap: 7px;
    height: 21px;
  }
  .contact-icon {
    width: 12px;
    height: 12px;
    fill: var(--accent-orange);
    stroke: var(--accent-orange);
  }
  .person {
    position: absolute;
    right: 24px;
    top: 183px;
    text-align: right;
  }
  .person-name {
    font-size: 26px;
    font-weight: 600;
    color: var(--accent-orange);
    line-height: 1.1;
  }
  .person-title {
    font-size: 18px;
    color: var(--text-grey);
    margin-top: 1px;
  }
  .back-brand {
    position: absolute;
    left: 0;
    right: 0;
    top: 112px;
    text-align: center;
    font-size: 68px;
    font-weight: 600;
    line-height: 1;
    color: var(--peach);
  }
  .services {
    position: absolute;
    left: 0;
    right: 0;
    top: 261px;
    text-align: center;
    font-size: 17.5px;
    color: var(--back-text);
    word-spacing: 1px;
  }
</style>
</head>
<body>
<main class="stage">
  <section class="card card-front">
    <div class="brand-mark">
      <span class="brand-dot"></span>
      <span class="brand-name">Torvane</span>
    </div>
    <div class="address">
      1234, Address Goes Here<br>
      Country Name, 123456
    </div>
    <ul class="contact-list">
      <li>
        <svg class="contact-icon" viewBox="0 0 12 12" aria-hidden="true">
          <path d="M1 4 Q6 0 11 4 L9 5 L8 3.5 L4 3.5 L3 5 Z" stroke="none"/>
          <rect x="2.5" y="6" width="7" height="4" rx="1" stroke="none"/>
        </svg>
        <span>123-456-7890</span>
      </li>
      <li>
        <svg class="contact-icon" viewBox="0 0 12 12" aria-hidden="true">
          <rect x="1" y="3" width="10" height="7" stroke="none"/>
          <path d="M1 3 L6 7 L11 3" fill="none" stroke="#fff" stroke-width="1"/>
        </svg>
        <span>info@youremail.com</span>
      </li>
      <li>
        <svg class="contact-icon" viewBox="0 0 12 12" aria-hidden="true">
          <path d="M5 7 L7 5 M4 5.5 L2.5 7 A1.8 1.8 0 0 0 5 9.5 L6.5 8 M8 6.5 L9.5 5 A1.8 1.8 0 0 0 7 2.5 L5.5 4" fill="none" stroke-width="1.4" stroke-linecap="round"/>
        </svg>
        <span>www.yourweb.com</span>
      </li>
    </ul>
    <div class="person">
      <div class="person-name">John Smith</div>
      <div class="person-title">Managing Director</div>
    </div>
  </section>

  <section class="card card-back">
    <div class="back-brand">Torvane</div>
    <div class="services">IT Strategist &nbsp;| ConsultantSystems &nbsp;| Infrastructure &nbsp;| &nbsp;Cybersecurity</div>
  </section>
</main>
</body>
</html>
```